Brookvale Renovations - Get the creative juices going!!

Brookvale does not do the actual renovation work. The company provides high end project management of renovation (primarily residential - with an eye toward commercial) The renovation work could look very different between projects. This company manages the work of contractors, architects and interior designers (either subcontracted directly by Brookvale or hired by the client and entrusted to Brookvale to manage). Clients are high end in the economic scale and the card needs to have a high end feel to it.

The owner is female, but the audience will be heavily slanted male. It should not be a "feminine" or "masculine" looking card. If anything, slant more on the masculine side. Clean, simple, yet creative and artistically appealing. The card design should complement and in no way compete with the logo.

When people think of our company: trust, integrity, dynamic, limitless possibilities, transition, energy, creative. We plan to expand in the future to be international.

There will also be a contest running for stationary. Please check that section, as well.

***Black is 80-90 percent black. Not stark black

Tight timeline. Needs cards printed quickly!

```html
<!DOCTYPE html>
<html lang="en">
<head>
<meta charset="utf-8">
<title>Brookvale Renovations – Business Card</title>
<link href="https://fonts.googleapis.com/css2?family=Questrial&family=Open+Sans:wght@400;600&display=swap" rel="stylesheet">
<style>
  :root {
    --charcoal: #2a2b2d;
    --charcoal-deep: #222325;
    --teal: #1fb5ad;
    --white: #ffffff;
    --ink: #3a3b3d;
    --mist: #e9eaec;
    --divider: #8a8c90;
  }
  * { box-sizing: border-box; margin: 0; padding: 0; }
  html, body { width: 1200px; height: 784px; overflow: hidden; }
  body {
    background: var(--mist);
    display: flex;
    align-items: center;
    justify-content: center;
    gap: 48px;
    font-family: "Open Sans", sans-serif;
  }
  .card {
    width: 530px;
    height: 303px;
    position: relative;
    overflow: hidden;
    box-shadow: 0 10px 28px rgba(0,0,0,.18);
  }
  /* back face */
  .card--back {
    background: linear-gradient(150deg, var(--charcoal) 0%, var(--charcoal-deep) 100%);
    display: flex;
    align-items: center;
    justify-content: center;
  }
  .brand {
    display: flex;
    align-items: center;
    gap: 12px;
    font-family: "Questrial", sans-serif;
    font-size: 30px;
    letter-spacing: 2px;
    text-transform: uppercase;
    white-space: nowrap;
  }
  .brand__mark { width: 16px; height: 16px; background: var(--teal); flex: none; }
  .card--back .brand { color: var(--white); }
  /* front face */
  .card--front { background: var(--white); }
  .front__top {
    height: 168px;
    display: flex;
    align-items: center;
    justify-content: center;
    padding-top: 20px;
  }
  .card--front .brand { color: var(--ink); font-size: 28px; }
  .front__band { height: 9px; background: var(--teal); }
  .front__bottom {
    position: absolute;
    left: 0; right: 0; bottom: 0;
    height: 126px;
    background: var(--charcoal);
    display: flex;
    align-items: center;
  }
  .person {
    width: 220px;
    text-align: right;
    padding-right: 22px;
  }
  .person__name {
    font-family: "Questrial", sans-serif;
    color: var(--teal);
    font-size: 19px;
    font-weight: 600;
  }
  .person__role { color: var(--white); font-size: 13px; margin-top: 2px; }
  .divider { width: 1px; height: 92px; background: var(--divider); }
  .contact {
    list-style: none;
    padding-left: 18px;
    color: var(--white);
    font-size: 12.5px;
    line-height: 18px;
  }
  .contact li { display: flex; align-items: flex-start; gap: 8px; }
  .contact svg { width: 12px; height: 12px; margin-top: 3px; flex: none; fill: var(--teal); }
</style>
</head>
<body>

  <section class="card card--back" aria-label="Card back">
    <div class="brand"><span class="brand__mark"></span>Brookvale Renovations</div>
  </section>

  <section class="card card--front" aria-label="Card front">
    <div class="front__top">
      <div class="brand"><span class="brand__mark"></span>Brookvale Renovations</div>
    </div>
    <div class="front__bottom">
      <div class="front__band" style="position:absolute;top:-9px;left:0;right:0;"></div>
      <div class="person">
        <p class="person__name">Daniel Harper</p>
        <p class="person__role">Managing Director</p>
      </div>
      <div class="divider"></div>
      <ul class="contact">
        <li>
          <svg viewBox="0 0 24 24"><path d="M6.6 10.8a15.1 15.1 0 0 0 6.6 6.6l2.2-2.2a1 1 0 0 1 1-.25 11.4 11.4 0 0 0 3.6.57 1 1 0 0 1 1 1V20a1 1 0 0 1-1 1A17 17 0 0 1 3 4a1 1 0 0 1 1-1h3.5a1 1 0 0 1 1 1c0 1.25.2 2.45.57 3.6a1 1 0 0 1-.25 1z"/></svg>
          <span>(501) 555-0142</span>
        </li>
        <li>
          <svg viewBox="0 0 24 24"><path d="M12 2a10 10 0 1 0 0 20 10 10 0 0 0 0-20zm6.9 6h-2.9a15.7 15.7 0 0 0-1.4-3.6A8 8 0 0 1 18.9 8zM12 4c.8 1.2 1.5 2.5 1.9 4h-3.8c.4-1.5 1.1-2.8 1.9-4zM4.3 14a8 8 0 0 1 0-4h3.4a16.5 16.5 0 0 0 0 4zm.8 2h2.9c.3 1.3.8 2.5 1.4 3.6A8 8 0 0 1 5.1 16zM8 8H5.1a8 8 0 0 1 4.3-3.6C8.8 5.5 8.3 6.7 8 8zm4 12c-.8-1.2-1.5-2.5-1.9-4h3.8c-.4 1.5-1.1 2.8-1.9 4zm2.3-6H9.7a14.7 14.7 0 0 1 0-4h4.6a14.7 14.7 0 0 1 0 4zm.3 5.6c.6-1.1 1.1-2.3 1.4-3.6h2.9a8 8 0 0 1-4.3 3.6zm1.7-5.6a16.5 16.5 0 0 0 0-4h3.4a8 8 0 0 1 0 4z"/></svg>
          <span>www.brookvalerenovations.com</span>
        </li>
        <li>
          <svg viewBox="0 0 24 24"><path d="M2 5h20v14H2zm2 2v.5l8 5 8-5V7zm16 2.8-8 5-8-5V17h16z"/></svg>
          <span>info@brookvalerenovations.com</span>
        </li>
        <li>
          <svg viewBox="0 0 24 24"><path d="M12 3 2 12h3v9h5v-6h4v6h5v-9h3z"/></svg>
          <span>Po Box 456, Harbour Road Belize,<br>NW 2710, Central America</span>
        </li>
      </ul>
    </div>
  </section>

</body>
</html>
```